Accounting business needs business card

I have a business card but need something better. I want the colour changed and the design to be better. I have uploaded a picture of my new sign that is grey in colour, i would like to incorporate these colours.

```html
<!DOCTYPE html>
<html lang="en">
<head>
<meta charset="utf-8">
<title>Level Ledger – Business Card</title>
<link rel="stylesheet" href="https://fonts.googleapis.com/css2?family=Montserrat:wght@400;500;600;700&display=swap">
<style>
  :root {
    --backdrop: #4a4a4a;
    --paper: #fbfbfb;
    --charcoal: #262626;
    --ink: #222222;
    --blue: #1ab3e8;
    --faint: #e4e4e4;
    --divider: #b8b8b8;
    --badge-navy: #1f4f9c;
    --badge-gold: #f2c417;
    --badge-green: #c9dc3a;
  }
  * { box-sizing: border-box; margin: 0; padding: 0; }
  html, body {
    width: 1200px; height: 900px; overflow: hidden;
    background: var(--backdrop);
    font-family: "Montserrat", sans-serif;
  }
  .canvas {
    position: relative; width: 1200px; height: 900px;
    display: flex; flex-direction: column; align-items: center; justify-content: center; gap: 44px;
  }
  .card {
    position: relative; width: 620px; height: 379px; overflow: hidden;
    box-shadow: 0 10px 24px rgba(0,0,0,.35);
  }

  /* Front: contact side */
  .card--front { background: var(--paper); color: var(--ink); }
  .front__watermark {
    position: absolute; left: 390px; top: -120px; width: 270px; height: 270px;
    border: 6px solid var(--faint); border-radius: 50%;
  }
  .front__brand { position: absolute; left: 40px; top: 34px; width: 270px; text-align: center; }
  .brand-dot {
    width: 62px; height: 62px; border: 2.5px solid var(--ink); border-radius: 50%;
    margin: 0 auto 14px;
  }
  .front__brand .brand-name {
    font-size: 22px; font-weight: 500; letter-spacing: 9px; padding-left: 9px; white-space: nowrap;
  }
  .person { position: absolute; left: 44px; top: 166px; }
  .person__name {
    color: var(--blue); font-weight: 700; font-size: 23px; letter-spacing: .5px; text-transform: uppercase;
  }
  .person__creds, .person__role { font-size: 14.5px; line-height: 21px; font-weight: 500; }
  .contacts { position: absolute; left: 48px; top: 262px; list-style: none; }
  .contacts li { display: flex; align-items: center; gap: 14px; height: 31px; font-size: 15.5px; font-weight: 500; }
  .contacts svg { width: 24px; height: 24px; flex: none; }

  .badges { position: absolute; right: 26px; bottom: 34px; display: flex; align-items: center; gap: 14px; }
  .badge-rect { width: 118px; height: 30px; display: flex; }
  .badge-rect span:first-child { flex: 3; background: var(--badge-navy); }
  .badge-rect span:last-child { flex: 2; background: var(--badge-gold); }
  .badge-seal { width: 50px; height: 50px; border-radius: 50%; border: 3px solid #d8d8d8; background: radial-gradient(circle, var(--badge-green) 0 38%, #fff 40%); }
  .badge-round { width: 50px; height: 50px; border-radius: 50%; background: var(--blue); }
  .badge-divider { width: 1.5px; height: 36px; background: var(--divider); transform: rotate(18deg); }

  /* Back: brand side */
  .card--back { background: var(--charcoal); color: var(--blue); }
  .back__brand { position: absolute; left: 0; right: 0; top: 38px; text-align: center; }
  .back__brand .brand-dot { width: 118px; height: 118px; border: 4px solid var(--blue); margin-bottom: 24px; }
  .back__brand .brand-name {
    font-size: 38px; font-weight: 600; letter-spacing: 16px; padding-left: 16px; white-space: nowrap;
  }
  .web-band {
    position: absolute; left: 0; right: 0; top: 262px; height: 46px;
    background: linear-gradient(90deg, #12ace6, var(--blue) 60%, #26bdf0);
    display: flex; align-items: center; justify-content: center;
  }
  .web-band a { color: var(--charcoal); text-decoration: none; font-weight: 700; font-size: 27px; letter-spacing: .3px; }
</style>
</head>
<body>
<main class="canvas">

  <section class="card card--front" aria-label="Business card, contact side">
    <div class="front__watermark" aria-hidden="true"></div>

    <div class="front__brand">
      <div class="brand-dot" aria-hidden="true"></div>
      <p class="brand-name">LEVEL LEDGER</p>
    </div>

    <div class="person">
      <h1 class="person__name">Owen Marsh</h1>
      <p class="person__creds">CPA, MTAX, B.COM (Acc &amp; Fin)</p>
      <p class="person__role">Taxation and Business Account</p>
    </div>

    <ul class="contacts">
      <li>
        <svg viewBox="0 0 24 24" aria-hidden="true"><circle cx="12" cy="12" r="10.5" fill="none" stroke="#1ab3e8" stroke-width="1.6"/><path d="M8.6 6.8l1.6 2.4-1 1.2a7 7 0 0 0 4.4 4.4l1.2-1 2.4 1.6-1 2c-4.8-.3-8.3-3.8-8.6-8.6z" fill="#1ab3e8"/></svg>
        0400 555 018
      </li>
      <li>
        <svg viewBox="0 0 24 24" aria-hidden="true"><circle cx="12" cy="12" r="10.5" fill="none" stroke="#1ab3e8" stroke-width="1.6"/><g fill="none" stroke="#1ab3e8" stroke-width="1.2"><circle cx="12" cy="12" r="6"/><ellipse cx="12" cy="12" rx="2.6" ry="6"/><path d="M6 12h12M7 9h10M7 15h10"/></g></svg>
        www.levelledger.com.au
      </li>
      <li>
        <svg viewBox="0 0 24 24" aria-hidden="true"><circle cx="12" cy="12" r="10.5" fill="none" stroke="#1ab3e8" stroke-width="1.6"/><rect x="6.5" y="8" width="11" height="8" rx="1" fill="#1ab3e8"/><path d="M6.8 8.4L12 12.4l5.2-4" fill="none" stroke="#fff" stroke-width="1"/></svg>
        owen@levelledger.com.au
      </li>
    </ul>

    <div class="badges" aria-label="Professional memberships">
      <div class="badge-rect" aria-hidden="true"><span></span><span></span></div>
      <div class="badge-divider" aria-hidden="true"></div>
      <div class="badge-seal" aria-hidden="true"></div>
      <div class="badge-divider" aria-hidden="true"></div>
      <div class="badge-round" aria-hidden="true"></div>
    </div>
  </section>

  <section class="card card--back" aria-label="Business card, brand side">
    <div class="back__brand">
      <div class="brand-dot" aria-hidden="true"></div>
      <p class="brand-name">LEVEL LEDGER</p>
    </div>
    <div class="web-band">
      <a href="#">www.levelledger.com.au</a>
    </div>
  </section>

</main>
</body>
</html>
```